Need a book cover design for a Lumora Book on Herbal Remedies

I need a book cover for my new ebook, here are the details:
Title: Meadow Cures
Sub-Heading: Buried Ancient Garden Tonics
Reclaiming the Wisdom of Roots for Everyday Wellness and Strength
Author: Nora Belcourt

```html
<!DOCTYPE html>
<html lang="en">
<head>
<meta charset="utf-8">
<title>Meadow Cures — Nora Belcourt</title>
<link rel="stylesheet" href="https://fonts.googleapis.com/css2?family=EB+Garamond:wght@400;700&family=Oswald:wght@700&family=Playball&family=Montserrat:wght@700&display=swap">
<style>
  :root {
    --backdrop: #c23a9f;
    --cover-cream: #f3e6d6;
    --title-green: #2f7a1f;
    --script-magenta: #a11a8a;
    --ink: #141414;
    --petal-plum: #7a1f45;
    --petal-violet: #b04ab8;
    --bloom-yellow: #e7cf6a;
    --leaf-green: #6f9a4a;
    --bowl-wood: #b8834e;
    --bloom-white: #f8f4ea;
  }
  * { margin: 0; padding: 0; box-sizing: border-box; }
  html, body { width: 1200px; height: 900px; overflow: hidden; }
  body { background: var(--backdrop); position: relative; }

  .cover {
    position: absolute; left: 331px; top: 19px;
    width: 537px; height: 861px;
    background: var(--cover-cream);
    overflow: hidden;
  }

  .botanical { position: absolute; }
  .botanical--bowl { border-radius: 50%; background: radial-gradient(circle, var(--bloom-yellow) 55%, var(--bowl-wood) 60%); }
  .botanical--bowl-dark { border-radius: 50%; background: radial-gradient(circle, #6e6a4c 55%, var(--bowl-wood) 60%); }
  .botanical--bowl-red { border-radius: 50%; background: radial-gradient(circle, #9a2a1c 55%, var(--bowl-wood) 60%); }
  .botanical--bloom { border-radius: 50%; background: radial-gradient(circle, var(--bloom-yellow) 15%, var(--petal-violet) 35%, rgba(122,31,69,0.0) 70%); }
  .botanical--daisy { border-radius: 50%; background: radial-gradient(circle, var(--bloom-yellow) 18%, var(--bloom-white) 25%, rgba(248,244,234,0) 70%); }
  .botanical--sprig { border-radius: 40%; background: radial-gradient(ellipse, rgba(111,154,74,0.85) 30%, rgba(111,154,74,0) 72%); }
  .botanical--clover { border-radius: 50%; background: radial-gradient(circle, var(--petal-violet) 30%, rgba(176,74,184,0) 70%); }
  .botanical--petals { border-radius: 50%; background: radial-gradient(circle, var(--petal-plum) 35%, rgba(122,31,69,0) 72%); }
  .botanical--yellow { border-radius: 50%; background: radial-gradient(ellipse, var(--bloom-yellow) 35%, rgba(231,207,106,0) 72%); }

  .series-line {
    position: absolute; left: 0; right: 0; top: 130px;
    text-align: center;
    font-family: "EB Garamond", serif; font-size: 26px; font-weight: 400;
    color: var(--ink);
  }
  .dot-rule {
    position: absolute; left: 148px; top: 191px; width: 240px; height: 6px;
  }
  .title-main {
    position: absolute; left: 0; right: 0; top: 224px;
    text-align: center;
    font-family: "Oswald", sans-serif; font-weight: 700;
    font-size: 150px; line-height: 1; letter-spacing: 1px;
    color: var(--title-green);
    text-shadow: 1px 2px 2px rgba(0,0,0,0.25);
  }
  .title-script {
    position: absolute; left: 0; right: 0; top: 392px;
    text-align: center;
    font-family: "Playball", cursive; font-size: 118px; line-height: 1.1;
    color: var(--script-magenta);
    text-shadow: 1px 2px 2px rgba(0,0,0,0.2);
  }
  .subtitle {
    position: absolute; left: 0; right: 0; top: 552px;
    text-align: center;
    font-family: "EB Garamond", serif; font-size: 27px; line-height: 34px;
    color: var(--ink);
  }
  .subtitle strong { font-weight: 700; }
  .author {
    position: absolute; left: 0; right: 0; top: 720px;
    text-align: center;
    font-family: "Montserrat", sans-serif; font-weight: 700;
    font-size: 28px; letter-spacing: 5px;
    color: var(--ink);
  }
</style>
</head>
<body>
  <main class="cover">
    <!-- top border -->
    <div class="botanical botanical--bowl" style="left:-20px;top:-20px;width:100px;height:130px;" role="img" aria-label="Wooden bowl of dried yellow flowers"></div>
    <div class="botanical botanical--daisy" style="left:85px;top:-5px;width:90px;height:90px;" role="img" aria-label="White chamomile daisy"></div>
    <div class="botanical botanical--bloom" style="left:250px;top:-30px;width:150px;height:140px;" role="img" aria-label="Purple poppy bloom with scattered petals"></div>
    <div class="botanical botanical--petals" style="left:195px;top:0;width:50px;height:50px;" role="img" aria-label="Dried rose petals"></div>
    <div class="botanical botanical--sprig" style="left:470px;top:-10px;width:80px;height:120px;" role="img" aria-label="Thyme sprig"></div>

    <!-- left border -->
    <div class="botanical botanical--bowl-dark" style="left:-12px;top:160px;width:60px;height:64px;" role="img" aria-label="Small bowl of dried cornflowers"></div>
    <div class="botanical botanical--daisy" style="left:-10px;top:280px;width:70px;height:110px;" role="img" aria-label="Feverfew flowers"></div>
    <div class="botanical botanical--petals" style="left:-15px;top:480px;width:55px;height:60px;" role="img" aria-label="Red nasturtium flower"></div>
    <div class="botanical botanical--sprig" style="left:-10px;top:560px;width:90px;height:150px;" role="img" aria-label="Yarrow and leafy herb sprigs"></div>
    <div class="botanical botanical--bowl-dark" style="left:-14px;top:690px;width:62px;height:60px;" role="img" aria-label="Bowl of dried green herbs"></div>

    <!-- right border -->
    <div class="botanical botanical--clover" style="left:460px;top:110px;width:70px;height:120px;" role="img" aria-label="Red clover blossom on a stem"></div>
    <div class="botanical botanical--clover" style="left:470px;top:260px;width:60px;height:80px;" role="img" aria-label="Foxglove bells"></div>
    <div class="botanical botanical--clover" style="left:490px;top:400px;width:40px;height:45px;" role="img" aria-label="Foxglove bell"></div>
    <div class="botanical botanical--bowl-dark" style="left:462px;top:443px;width:72px;height:72px;" role="img" aria-label="Bowl of dried root pieces"></div>
    <div class="botanical botanical--yellow" style="left:450px;top:530px;width:100px;height:120px;" role="img" aria-label="Meadowsweet cluster"></div>
    <div class="botanical botanical--bowl-red" style="left:495px;top:640px;width:60px;height:60px;" role="img" aria-label="Bowl of dried red herbs"></div>

    <!-- bottom border -->
    <div class="botanical botanical--petals" style="left:50px;top:760px;width:120px;height:60px;" role="img" aria-label="Scattered dried rose petals"></div>
    <div class="botanical botanical--clover" style="left:-10px;top:780px;width:110px;height:90px;" role="img" aria-label="Valerian flower heads"></div>
    <div class="botanical botanical--yellow" style="left:130px;top:790px;width:180px;height:90px;" role="img" aria-label="Yellow flower bloom"></div>
    <div class="botanical botanical--clover" style="left:335px;top:790px;width:75px;height:75px;" role="img" aria-label="Red clover blossom"></div>
    <div class="botanical botanical--petals" style="left:455px;top:700px;width:80px;height:60px;" role="img" aria-label="Scattered dried rose petals"></div>
    <div class="botanical botanical--sprig" style="left:450px;top:780px;width:90px;height:90px;" role="img" aria-label="Honeysuckle flower"></div>

    <p class="series-line">Buried Ancient Garden Tonics</p>
    <svg class="dot-rule" viewBox="0 0 240 6" aria-hidden="true">
      <g fill="#141414">
        <circle cx="3" cy="3" r="2.6"/><circle cx="16" cy="3" r="2.6"/><circle cx="29" cy="3" r="2.6"/><circle cx="42" cy="3" r="2.6"/><circle cx="55" cy="3" r="2.6"/><circle cx="68" cy="3" r="2.6"/><circle cx="81" cy="3" r="2.6"/><circle cx="94" cy="3" r="2.6"/><circle cx="107" cy="3" r="2.6"/><circle cx="120" cy="3" r="2.6"/><circle cx="133" cy="3" r="2.6"/><circle cx="146" cy="3" r="2.6"/><circle cx="159" cy="3" r="2.6"/><circle cx="172" cy="3" r="2.6"/><circle cx="185" cy="3" r="2.6"/><circle cx="198" cy="3" r="2.6"/><circle cx="211" cy="3" r="2.6"/><circle cx="224" cy="3" r="2.6"/><circle cx="237" cy="3" r="2.6"/>
      </g>
    </svg>
    <h1>
      <span class="title-main">MEADOW</span>
      <span class="title-script">Cures</span>
    </h1>
    <p class="subtitle"><strong>Reclaiming</strong> the Wisdom<br>of <strong>Roots</strong> for Everyday<br><strong>Wellness and Strength</strong></p>
    <p class="author">NORA BELCOURT</p>
  </main>
</body>
</html>
```